Conservative, Modern and Sharp Builder Business card

Hi there,
We would like to update our existing business card.
I have attached photos of existing business card, logo and van sign.

I would like the business card to also list what we do :
Renovation • New Build • Alteration
Extension • Bathroom • Maintenance.(Seperated by dots)

Contact number : 021 0483 0752
(With that exact spacing)

Ideally when people looking from about 2-3 metres, they know that it is a builder’s business card

Open to suggestions on fonts, layout, style of business card

PLEASE ONLY SUBMIT YOUR BEST OR MAX 3 DESIGNS FOR EACH DESIGNER

Thanks

Industry/Entity Type

Construction. Renovation

Contact Information for Business Card

Details should be the same as the existing card. And addition of what we do.

Requirements
Should not have
• The new business card must not have the same layout as our existing one. Thanks

```html
<!DOCTYPE html>
<html lang="en">
<head>
<meta charset="utf-8">
<title>KeelBuild Business Card</title>
<link rel="stylesheet" href="https://fonts.googleapis.com/css2?family=Open+Sans:wght@400;600;700;800&display=swap">
<style>
  :root {
    --backdrop: #d9d6d2;
    --card-black: #1e1f22;
    --card-deep: #151619;
    --band-mid: #1a1b1e;
    --band-low: #17181a;
    --ink-white: #ffffff;
    --ink-soft: #e9e9ea;
    --pattern-silver: #8c8d90;
  }
  * { margin: 0; padding: 0; box-sizing: border-box; }
  html, body {
    width: 1200px; height: 780px; overflow: hidden;
    background: var(--backdrop);
    font-family: "Open Sans", Arial, sans-serif;
  }
  .canvas {
    position: relative; width: 1200px; height: 780px;
    display: flex; justify-content: center; align-items: center; gap: 80px;
  }
  .card {
    position: relative; width: 380px; height: 660px;
    background: var(--card-black); border-radius: 4px; overflow: hidden;
    box-shadow: 0 10px 26px rgba(0,0,0,.28);
  }

  /* Front */
  .front-pattern {
    position: absolute; inset: 0;
    background:
      radial-gradient(ellipse at 0% 0%, rgba(170,171,175,.55) 0%, rgba(90,91,95,.25) 35%, rgba(0,0,0,0) 62%),
      linear-gradient(160deg, #2a2b2e 0%, var(--card-deep) 55%, #0f1012 100%);
  }
  .front-brand {
    position: absolute; left: 50%; top: 50%;
    transform: translate(-50%, -50%) rotate(-90deg);
    display: flex; align-items: center; gap: 18px;
    white-space: nowrap;
  }
  .front-brand .brand-dot {
    width: 54px; height: 54px; border-radius: 50%; background: var(--ink-white);
  }
  .front-brand .brand-name {
    font-weight: 800; font-size: 70px; color: var(--ink-white); letter-spacing: -1px;
  }

  /* Back */
  .back-bands { position: absolute; inset: 0; width: 100%; height: 100%; }
  .back-brand {
    position: absolute; top: 70px; left: 0; right: 0;
    display: flex; flex-direction: column; align-items: center; gap: 16px;
  }
  .back-brand .brand-dot {
    width: 70px; height: 70px; border-radius: 50%; background: var(--ink-white);
  }
  .back-brand .brand-name {
    font-weight: 800; font-size: 44px; color: var(--ink-white); letter-spacing: -.5px;
  }
  .person {
    position: absolute; top: 222px; left: 0; right: 0; text-align: center; color: var(--ink-white);
  }
  .person-name { font-weight: 700; font-size: 27px; line-height: 1.1; }
  .person-role { font-weight: 600; font-size: 16px; color: var(--ink-soft); margin-top: 2px; }
  .contact-icons {
    display: flex; justify-content: center; gap: 8px; margin-top: 12px;
  }
  .contact-icons .icon {
    width: 26px; height: 26px; border-radius: 50%; background: var(--ink-white);
    display: flex; align-items: center; justify-content: center;
  }
  .contact-lines {
    margin-top: 10px; list-style: none;
    font-size: 16px; line-height: 1.32; color: var(--ink-soft);
  }
  .services {
    position: absolute; left: 0; right: 0; bottom: 46px; text-align: center; color: var(--ink-white);
  }
  .services-tag {
    display: inline-block; background: var(--ink-white); color: var(--card-deep);
    font-weight: 700; font-size: 14px; padding: 5px 20px; border-radius: 50%;
    margin-bottom: 10px;
  }
  .services-list { list-style: none; font-size: 17px; line-height: 1.45; font-weight: 600; }
</style>
</head>
<body>
<main class="canvas">

  <section class="card card-front" aria-label="Card front">
    <div class="front-pattern" role="img" aria-label="Repeating monogram pattern fading from silver at the top left into black"></div>
    <div class="front-brand">
      <span class="brand-dot"></span>
      <span class="brand-name">KeelBuild</span>
    </div>
  </section>

  <section class="card card-back" aria-label="Card back">
    <svg class="back-bands" viewBox="0 0 380 660" preserveAspectRatio="none" aria-hidden="true">
      <path d="M0 470 Q 190 520 380 330 L380 660 L0 660 Z" fill="var(--band-mid)"/>
      <path d="M0 545 Q 230 560 380 420 L380 660 L0 660 Z" fill="var(--band-low)"/>
      <path d="M0 470 Q 190 520 380 330" fill="none" stroke="#2a2b2f" stroke-width="1"/>
    </svg>

    <header class="back-brand">
      <span class="brand-dot"></span>
      <span class="brand-name">KeelBuild</span>
    </header>

    <div class="person">
      <h1 class="person-name">Toma Varen</h1>
      <p class="person-role">Residential Builder</p>
      <div class="contact-icons">
        <span class="icon">
          <svg width="14" height="14" viewBox="0 0 24 24" aria-hidden="true"><path d="M6.6 10.8a15 15 0 0 0 6.6 6.6l2.2-2.2a1 1 0 0 1 1-.25 11.4 11.4 0 0 0 3.6.57 1 1 0 0 1 1 1V20a1 1 0 0 1-1 1A17 17 0 0 1 3 4a1 1 0 0 1 1-1h3.5a1 1 0 0 1 1 1c0 1.25.2 2.45.57 3.6a1 1 0 0 1-.25 1z" fill="#151619"/></svg>
        </span>
        <span class="icon"></span>
        <span class="icon">
          <svg width="14" height="14" viewBox="0 0 24 24" aria-hidden="true"><rect x="3" y="6" width="18" height="12" rx="1" fill="none" stroke="#151619" stroke-width="2"/><path d="M3 7l9 6 9-6" fill="none" stroke="#151619" stroke-width="2"/></svg>
        </span>
        <span class="icon">
          <svg width="14" height="14" viewBox="0 0 24 24" aria-hidden="true"><circle cx="12" cy="12" r="9" fill="none" stroke="#151619" stroke-width="2"/><path d="M3 12h18M12 3c3 3 3 15 0 18M12 3c-3 3-3 15 0 18" fill="none" stroke="#151619" stroke-width="1.6"/></svg>
        </span>
      </div>
      <ul class="contact-lines">
        <li>021 0483 0752</li>
        <li>KeelBuild.nz</li>
        <li>www.KeelBuild.nz</li>
        <li>hello@keelbuild.nz</li>
      </ul>
    </div>

    <div class="services">
      <span class="services-tag">WHAT WE DO</span>
      <ul class="services-list">
        <li>• Renovation • New Build • Alteration</li>
        <li>• Extension • Bathroom • Maintenance</li>
      </ul>
    </div>
  </section>

</main>
</body>
</html>
```